Business Card Design

I am a self-employed qualified carpenter with the business name Brankwell Joinery. I would like to incorporate the attached logo with a black background with white writing and keep the blue and green that is in my logo if possible.

Industry/Entity Type

Business

Contact Information for Business Card

The attached logo Brankwell Joinery. Marcus Penhallow, Qualified Carpenter, mobile number 0478 562 914, email markpenhallow@quillbox.net, postal address PO Box 617 TARLEE VIC 3291, ABN 47 683 920 514.

```html
<!DOCTYPE html>
<html lang="en">
<head>
<meta charset="utf-8">
<title>Brankwell Joinery – Business Card</title>
<link href="https://fonts.googleapis.com/css2?family=Montserrat:wght@400;500;700;800&display=swap" rel="stylesheet">
<style>
  :root {
    --page-bg: #ffffff;
    --card-bg: #3a3a3c;
    --text-light: #ffffff;
    --accent-green: #2fb468;
    --accent-teal: #06b6b0;
    --divider-shadow: rgba(0, 0, 0, 0.55);
  }
  * { margin: 0; padding: 0; box-sizing: border-box; }
  html, body {
    width: 1200px;
    height: 1000px;
    overflow: hidden;
    background: var(--page-bg);
    font-family: "Montserrat", Arial, sans-serif;
  }
  .card {
    position: absolute;
    left: 208px;
    top: 258px;
    width: 783px;
    height: 483px;
    background: var(--card-bg);
    color: var(--text-light);
    overflow: hidden;
  }
  .brand {
    position: absolute;
    left: 60px;
    top: 190px;
    width: 330px;
    text-align: center;
  }
  .brand-name {
    font-weight: 800;
    font-size: 44px;
    line-height: 44px;
    letter-spacing: -1px;
    color: var(--text-light);
  }
  .brand-note {
    margin-top: 6px;
    font-size: 14px;
    font-weight: 400;
  }
  .divider {
    position: absolute;
    left: 428px;
    top: 70px;
    width: 4px;
    height: 340px;
    background: linear-gradient(to right, var(--divider-shadow), transparent);
  }
  .name-band {
    position: absolute;
    left: 430px;
    top: 95px;
    width: 353px;
    height: 80px;
    padding: 18px 0 0 20px;
    background: linear-gradient(to right, var(--accent-green), var(--accent-teal));
  }
  .person-name {
    font-weight: 700;
    font-size: 24px;
    line-height: 28px;
    letter-spacing: 0.3px;
  }
  .person-role {
    font-size: 16px;
    font-weight: 400;
    line-height: 20px;
  }
  .contact-row {
    position: absolute;
    left: 430px;
    display: flex;
    align-items: flex-start;
  }
  .contact-icon {
    flex: none;
    width: 55px;
    height: 41px;
    display: flex;
    align-items: center;
    justify-content: center;
    background: linear-gradient(to right, var(--accent-green), var(--accent-teal));
  }
  .contact-text {
    margin-left: 15px;
    font-size: 19px;
    font-weight: 500;
    line-height: 41px;
    letter-spacing: 0.3px;
    white-space: nowrap;
  }
  .contact-text.email {
    font-size: 17px;
    letter-spacing: 0;
  }
  .contact-text.address {
    margin-left: 10px;
    line-height: 25px;
    margin-top: 3px;
  }
  .row-phone { top: 198px; }
  .row-email { top: 253px; }
  .row-address { top: 309px; }
</style>
</head>
<body>
  <main class="card">
    <div class="brand">
      <div class="brand-name">Brankwell<br>Joinery</div>
      <div class="brand-note">(will be replaced with logo)</div>
    </div>

    <div class="divider"></div>

    <header class="name-band">
      <div class="person-name">MARCUS PENHALLOW</div>
      <div class="person-role">Qualified Carpenter</div>
    </header>

    <div class="contact-row row-phone">
      <span class="contact-icon">
        <svg width="18" height="30" viewBox="0 0 18 30" aria-hidden="true">
          <rect x="1" y="1" width="16" height="28" rx="3" fill="none" stroke="#fff" stroke-width="2"/>
          <line x1="1" y1="5" x2="17" y2="5" stroke="#fff" stroke-width="1.5"/>
          <line x1="1" y1="23" x2="17" y2="23" stroke="#fff" stroke-width="1.5"/>
          <circle cx="9" cy="26" r="1.4" fill="#fff"/>
        </svg>
      </span>
      <span class="contact-text">0478 562 914</span>
    </div>

    <div class="contact-row row-email">
      <span class="contact-icon">
        <svg width="20" height="14" viewBox="0 0 20 14" aria-hidden="true">
          <rect x="0" y="0" width="20" height="14" fill="#fff"/>
          <polyline points="0,0 10,8 20,0" fill="none" stroke="#1fb58c" stroke-width="1.5"/>
        </svg>
      </span>
      <span class="contact-text email">markpenhallow@quillbox.net</span>
    </div>

    <div class="contact-row row-address">
      <span class="contact-icon">
        <svg width="20" height="26" viewBox="0 0 20 26" aria-hidden="true">
          <path d="M10 24 C4 17 2 13 2 9.5 A8 8 0 0 1 18 9.5 C18 13 16 17 10 24 Z" fill="none" stroke="#fff" stroke-width="2"/>
          <circle cx="10" cy="9.5" r="3" fill="none" stroke="#fff" stroke-width="2"/>
        </svg>
      </span>
      <span class="contact-text address">PO Box 617<br>TARLEE VIC 3291,<br>ABN 47 683 920 514.</span>
    </div>
  </main>
</body>
</html>
```